Velmar Computers Brochure design

We need an brochure, in a4 size, it should be 8 pages in total.

We have 9 topics we need covered:
Front page
Velmar introduction
Velmar office series
Velmar Business series
Velmar Performance series
Partners
Oxbrin
Warranty
Contact details, Back page

WE have a new material we want to use instead of the current oxbrin page:

https://www.filecrate-example.com/s/qp7rmxwatg3kzn2/OXBRIN.pdf

• I have added a PowerPoint presentation with information we want in the brochure. There are 9 pages, so if you can merge two of them together to one so we get a total of 8 pages.

I have also added pictures of TQ screens, that can be bundled with all our machines. We also want that to be shown some where, maybe on same page as the computers.

```html
<!DOCTYPE html>
<html lang="en">
<head>
<meta charset="utf-8">
<title>Velmar Computers – Warranty &amp; Partners</title>
<link rel="stylesheet" href="https://fonts.googleapis.com/css2?family=Open+Sans:wght@400;600;700&display=swap">
<style>
  :root {
    --deep-blue: #0e5590;
    --mid-blue: #1f7fbf;
    --cyan: #22e4f2;
    --white: #ffffff;
    --panel-top: #f6f7f4;
    --panel-bottom: #a9b5a3;
    --panel-right-top: #a7b5a3;
    --heading-blue: #3b5fd8;
    --heading-navy: #1c5c8c;
    --body-text: #262626;
    --badge-blue: #2f6fb8;
    --badge-edge: #8fb4d8;
  }
  * { box-sizing: border-box; margin: 0; padding: 0; }
  html, body { width: 1200px; height: 849px; overflow: hidden; }
  body {
    font-family: "Open Sans", Arial, sans-serif;
    color: var(--body-text);
    background: var(--white);
  }
  .spread {
    position: relative;
    width: 1200px;
    height: 849px;
    overflow: hidden;
    background: linear-gradient(180deg, var(--deep-blue) 0%, var(--deep-blue) 18%, var(--mid-blue) 28%, var(--cyan) 45%, #9ff3f8 62%, var(--white) 78%);
  }
  .mosaic-backdrop {
    position: absolute;
    left: 0; top: 110px;
    width: 1200px; height: 600px;
    background:
      radial-gradient(ellipse 520px 160px at 900px 120px, rgba(14,85,144,0.55), transparent 70%),
      radial-gradient(ellipse 700px 220px at 600px 300px, rgba(34,228,242,0.5), transparent 75%);
  }
  .brand-name {
    position: absolute;
    left: 193px; top: 46px;
    font-size: 54px;
    font-weight: 700;
    letter-spacing: 1px;
    color: var(--white);
    line-height: 1;
  }
  .panel {
    position: absolute;
    width: 334px;
  }
  .panel--warranty {
    left: 143px; top: 130px; height: 719px;
    background: linear-gradient(180deg, var(--white) 0%, var(--panel-top) 12%, #dfe3da 45%, var(--panel-bottom) 100%);
    box-shadow: 0 -6px 14px 6px rgba(255,255,255,0.8);
  }
  .panel--partners {
    left: 750px; top: 0; height: 625px;
    background: linear-gradient(180deg, var(--panel-right-top) 0%, #bfc9b9 20%, #e4e9e1 60%, var(--white) 96%);
    box-shadow: 0 4px 8px rgba(0,0,0,0.18);
  }
  .panel-inner { position: absolute; left: 16px; right: 14px; }
  .panel--warranty .panel-inner { top: 18px; }
  .panel--partners .panel-inner { top: 148px; left: 9px; right: 16px; }
  .panel-title {
    font-size: 20px;
    font-weight: 600;
    line-height: 24px;
    margin-bottom: 47px;
  }
  .panel--warranty .panel-title { color: var(--heading-blue); }
  .panel--partners .panel-title { color: var(--heading-navy); }
  .section-title {
    font-size: 11.5px;
    font-weight: 600;
    color: var(--heading-navy);
    margin-bottom: 12px;
  }
  .body-copy {
    font-size: 9.1px;
    line-height: 14.3px;
    margin-bottom: 11px;
  }
  .body-copy strong { font-weight: 700; }
  .reason-list { list-style: none; }
  .reason-list li {
    position: relative;
    padding-left: 12px;
    font-size: 9.1px;
    line-height: 14.3px;
    margin-bottom: 11px;
  }
  .reason-list svg {
    position: absolute; left: 0; top: 2px;
    width: 7px; height: 10px;
  }
  .partners-section { margin-top: 18px; }
  .badge-row {
    position: absolute;
    left: 817px; top: 675px;
    display: flex; gap: 16px;
  }
  .partner-badge {
    width: 61px; height: 46px;
    border-radius: 4px;
    background: linear-gradient(180deg, #5d93cf, var(--badge-blue));
    border: 2px solid var(--badge-edge);
  }
  .os-partner-name {
    position: absolute;
    left: 847px; top: 738px;
    width: 170px;
    text-align: center;
    font-size: 26px;
    font-weight: 400;
    line-height: 32px;
    color: var(--heading-navy);
  }
</style>
</head>
<body>
<main class="spread">
  <div class="mosaic-backdrop" role="img" aria-label="Decorative pixel mosaic fading from deep blue to cyan and white"></div>

  <div class="brand-name">VELMAR</div>

  <section class="panel panel--warranty">
    <div class="panel-inner">
      <h1 class="panel-title">Warranty</h1>
      <h2 class="section-title">Customer support</h2>
      <p class="body-copy">It is our upmost priority to provide the best possible service to our customers.</p>
      <p class="body-copy">We provide a 2 year warranty on all VELMAR products with a 5 working days repair guarantee. If a customer return a faulty VELMAR product to us and we cannot repair it within a maximum of 5 working days, we will simply either replace it with a new product or issue a refund of the purchase value. A 3 year warranty can be issued at an additional cost.</p>
      <p class="body-copy">These are some of the reasons why you should expect the very best support from us on VELMAR products:</p>
      <ul class="reason-list">
        <li><svg viewBox="0 0 7 10" aria-hidden="true"><path d="M1 1 L5.5 5 L1 9" fill="none" stroke="#111" stroke-width="1.8"/></svg>We always have stock of spare parts. You will never have to wait for spare parts to get shipped to Tanzania.</li>
        <li><svg viewBox="0 0 7 10" aria-hidden="true"><path d="M1 1 L5.5 5 L1 9" fill="none" stroke="#111" stroke-width="1.8"/></svg>We produced the product. That means we know it better than anyone and that we will be able to fix any issues you may experience. We have a highly qualified technical team that will be able to assist you.</li>
        <li><svg viewBox="0 0 7 10" aria-hidden="true"><path d="M1 1 L5.5 5 L1 9" fill="none" stroke="#111" stroke-width="1.8"/></svg>We make support an easy and pleasant experience to our customers. We always pick our phones within our office hours, we always respond to email queries right away and we make sure to keep the customer updated on the status of the support process.</li>
        <li><svg viewBox="0 0 7 10" aria-hidden="true"><path d="M1 1 L5.5 5 L1 9" fill="none" stroke="#111" stroke-width="1.8"/></svg>Should a reseller not provide sufficient support to the end user, the end user will always be able to contact us directly and get support from us.</li>
      </ul>
    </div>
  </section>

  <section class="panel panel--partners">
    <div class="panel-inner">
      <h1 class="panel-title">Partners</h1>
      <h2 class="section-title">The Components</h2>
      <p class="body-copy">We only select the very best manufacturers of the components used in the assembly These are the same vendors that are supplying parts to some of the largest international computer brands. This ensures that all our products are fitted with the best quality and newest technology available.</p>
      <p class="body-copy">For instance we use motherboards with built in antistatic protection and power supplies that have active power factor correction ability, allowing them to correct for most power fluctuations.</p>
      <p class="body-copy">We only offer the very latest technology. This means that you will</p>
      <div class="partners-section">
        <h2 class="section-title">International Partners</h2>
        <p class="body-copy">Velmar Computers is an official <strong>Oxbrin® Technology Provider Partner</strong>. This means that we are continuously working with Oxbrin® to provide you the most recent hardware available on the market.</p>
        <p class="body-copy">VELMAR is an authorized <strong>Corvane® OEM Partner</strong>. This means that we are able to provide you with genuine Corvane products as well as up-to-date support. As an OEM partner we have all the tools to offer you customized preloaded operating systems, such as Skylite® 7 and Skylite® 8, as well as drivers.</p>
      </div>
    </div>
  </section>

  <div class="badge-row">
    <div class="partner-badge" role="img" aria-label="Processor partner badge"></div>
    <div class="partner-badge" role="img" aria-label="Processor partner badge"></div>
    <div class="partner-badge" role="img" aria-label="Processor partner badge"></div>
  </div>

  <div class="os-partner-name">Skylite</div>
</main>
</body>
</html>
```